International Luxury Furniture and Accessories Outsourcing Company

We Need a Business Card design for a new Outsourcing company doing Business Internationally in the Luxury Furniture and Accessories Space. The company's name is GARETH VELLOR and we deal with clients in the high end and Luxury Space for Furniture and Accessories in the world. We would like Designs that speaks Luxury and Professionalism.

We like the Combination of the color Brown and Gold or Black and Gold. We are also open to other color combo.

We like some of the design of file attached.
Updates

This is Marcus and We really appreciate all of you taking the time out and putting the effort to help us jump start our new company. We have 2-3 designs that we like and will decide soon to pick one. Once again, Thank you to all of you !! Best Regards, Marcus

Industry/Entity Type

Business

```html
<!DOCTYPE html>
<html lang="en">
<head>
<meta charset="utf-8">
<title>Gareth Vellor – Business Card</title>
<link rel="stylesheet" href="https://fonts.googleapis.com/css2?family=Questrial&family=Open+Sans:wght@400;600;700&display=swap">
<style>
  :root {
    --backdrop: #2a2a2a;
    --card-dark: #1f1d1a;
    --card-light: #f7f7f5;
    --gold: #d8a833;
    --ink: #2b2b2b;
    --ink-soft: #3a3a3a;
    --silver: #e6e6e6;
  }
  * { margin: 0; padding: 0; box-sizing: border-box; }
  html, body {
    width: 1200px;
    height: 900px;
    overflow: hidden;
    background: var(--backdrop);
  }
  .canvas {
    width: 1200px;
    height: 900px;
    display: flex;
    flex-direction: column;
    align-items: center;
    justify-content: center;
    gap: 40px;
  }
  .card {
    width: 700px;
    height: 400px;
    position: relative;
    display: flex;
    flex-direction: column;
    align-items: center;
    box-shadow: 0 10px 30px rgba(0,0,0,.45);
  }
  .card--back { background: var(--card-dark); justify-content: center; }
  .card--front { background: var(--card-light); padding-top: 62px; }

  .brand {
    display: flex;
    flex-direction: column;
    align-items: center;
  }
  .brand-dot {
    width: 34px;
    height: 34px;
    border-radius: 50%;
    background: var(--gold);
    margin-bottom: 22px;
  }
  .brand-name {
    font-family: "Questrial", sans-serif;
    font-size: 44px;
    letter-spacing: 1px;
    line-height: 1;
  }
  .brand-tagline {
    font-family: "Questrial", sans-serif;
    font-size: 17px;
    letter-spacing: 1.2px;
    margin-top: 6px;
  }
  .card--back .brand-name,
  .card--back .brand-tagline { color: var(--silver); }
  .card--front .brand-name { color: var(--ink); }
  .card--front .brand-tagline { color: var(--ink-soft); }

  .holder {
    margin-top: 30px;
    text-align: center;
    font-family: "Open Sans", sans-serif;
  }
  .holder-name {
    color: var(--gold);
    font-weight: 700;
    font-size: 17px;
    letter-spacing: .5px;
  }
  .holder-role {
    color: var(--ink-soft);
    font-size: 14px;
    margin-top: 2px;
  }

  .contact {
    position: absolute;
    bottom: 34px;
    left: 0;
    right: 0;
    text-align: center;
    font-family: "Open Sans", sans-serif;
    font-size: 13px;
    color: var(--ink-soft);
  }
  .contact-label { color: var(--gold); font-weight: 600; }
  .contact-sep { margin: 0 5px; }
</style>
</head>
<body>
  <main class="canvas">
    <section class="card card--back" aria-label="Card back">
      <div class="brand">
        <span class="brand-dot"></span>
        <span class="brand-name">GARETH VELLOR</span>
        <span class="brand-tagline">FURNITURE AND ACCESSORIES</span>
      </div>
    </section>

    <section class="card card--front" aria-label="Card front">
      <div class="brand">
        <span class="brand-dot"></span>
        <span class="brand-name">GARETH VELLOR</span>
        <span class="brand-tagline">FURNITURE AND ACCESSORIES</span>
      </div>
      <div class="holder">
        <p class="holder-name">MARCUS HALE</p>
        <p class="holder-role">General Manager</p>
      </div>
      <p class="contact">
        <span class="contact-label">T:</span> (+61) 03 5550 0147<span class="contact-sep">·</span><span class="contact-label">E:</span> marcus@garethvellor.com<span class="contact-sep">·</span><span class="contact-label">W:</span> www.garethvellor.com
      </p>
    </section>
  </main>
</body>
</html>
```